Cresthaven Vale Goods & City of Nyssa; Public Forum: "Community in Action & Economic Deve...

To Whom it may concern; My name is Garrett Lyle Pascoe and I am the owner of Cresthaven Vale Goods LLC. I live in eastern Oregon in a town called Ontario. I'm originally from a smaller town 12 miles south of Ontario called Nyssa Oregon and that's where this project or the location of my business is going to be located along with moving my family. My Grandfather started a Beer & Pascoe Wholesaler in 1965 in Nyssa called Marlbrook Supply, my father was second generation owner and I had always planned on being 3rd. Well, with big business changing how things work with business consolidating to spread the cost of debt and Dravco purchase of Kessling Morrow, I wouldn't have been approved to buy(franchise agreement). So, bare with me, I tell you this because this information that you'll need to know for the project. My grandfather and Father built a legacy in Nyssa Oregon and were known for; Ethics and Morals, involvement in the community, fundraisers, donations, charity work, public service (volunteer firefighters), endowment scholarship fundraisers, etc....so my grandfather and dad were and are a big fish in a little pond but both are my hero's.

For the last 17 years I've been involved with the State Medical Marijuana program SMMP. Its operated through; BWA; Bureau of Welfare Affairs @ SCA; State Care Agency. I have seen many changes throughout the program. I have a Medical Marijuana Patient card, several Medical Marijuana Caregiver cards, grower cards but the grower cards have been replaced with a Grow Site Administrator card and I am a GSA. So my trade has been indoor cultivation and growing for patients who aren't able due to either health or the financial burdens that an indoor grow requires. Helping others (patients) find relief in whatever aliment they might be fighting has been very rewarding and I love the science behind growing.
In 2015 Oregon passed reactional Marijuana and it is ran by the SSRB; State Spirits Regulation Board. Governor Kessel of Oregon gave local government (city council) the option of opting out of the program which has a 6 tier system with different licensing. Malheur County in which I lived opted out immediately along with Ontario and Nyssa Oregon. Well, Ontario Oregon lifted the ban about 1 year ago and it was a battle but people have slowly started to sway their opinion towards Cannabis. But, now Ontario Oregon is receiving all of the tax benefits that the SSRB program has to offer along with some city sales taxes on the product and Ontario is thriving. Malheur County and the cities within are the poorest in the state, so the tax benefits will go a long way.

PROJECT; I'm a family man.. my wife and I have 4 kids and have decided to move out of Ontario and to my home town in Nyssa (12 miles south of Ontario). I have been working with the community of Nyssa and the City of Nyssa (City Council, Police Department, Fire Department and Chamber of Commerce) in lifting the ban on reactional Marijuana in Nyssa Oregon. I am only asking for 2 out of the 6 licenses and will explain that along with the local politics and my business plan with some attachments. I have done my homework and leg work with this project but ran into an issue and this Is why I'm seeking outside help on the development of a power point. I finally reached my last step, in which was my presentation to the community and city council. I had put together a power point myself and used that for my presentation (I will send you this power point as well). .

I'm going to be having a Public Forum held In Nyssa Oregon so I can get the community to come out and get the right information and ask questions...I was going to see if you guys would design me a power point presentation....I do have one, but I really want a more professional touch...I can send you; business plan, city council power point and some other information....

Thanks,
Garrett Lyle Pasco
Cresthaven Vale Goods

Target Market(s)

Nyssa Oregon City Council Members and the Community/Citizens of Nyssa Oregon

Font styles to use
Sans Serif

Colors

Designer to choose only greyscale colors for use in the design.

Requirements
Must have
• bullet points; on key topics showing what our intent is and what isn't our intent
• heart and passion; getting Nyssa in which is directly on the border with Idaho who is illegal in both medical and recreational marijuana has been huge. Getting the band lifted the Governor Kessel gave city or counties the option to do has been a daunting task.
• Clarity with no chance of misunderstanding my company's intent; i can send you folks some articles and a power point that i put together for the city council as reference.
• market analysis section; so not only will we be talking about the 3% city sales tax on either my recreational production license or the wholesale license, but we will be my company is donating another 3% with our Neighbourhood Uplift Giving Pool. Also, if we can't get a city sales tax on one of those licenses then my company pledges to up our neighbourhood uplift giving pool another 3% to make that a 6% donation on monthly profits. finally, i would like to show the community of Nyssa in visual aids such as graphs,a basic market analysis on what the state of oregon has been bringing in with the tax benefits from recreational marijuana, the city of Huntington Oregon (close to Ontario and opened up their market a couple years before Ontario Oregon did) and finally Ontario Oregon (12 miles north from Nyssa Oregon) and what they have been bringing in with the tax benefits.
Nice to have
• company logo
• pictures of my family
• pictures of Nyssa Oregon
• some positive uplifting quotes on change, trust and family
Should not have
• no Pictures of Marijuana (out of sight out of mind)

```html
<!DOCTYPE html>
<html lang="en">
<head>
<meta charset="utf-8">
<title>Cresthaven Vale Goods – Presentation Deck</title>
<link href="https://fonts.googleapis.com/css2?family=Barlow:wght@300;400;500;600;700&family=Poppins:wght@300;400;700&display=swap" rel="stylesheet">
<style>
:root{
  --gold:#f0ad3c;
  --gold-soft:#f4c05a;
  --gold-pale:#f8d89a;
  --navy:#1d4a66;
  --navy-deep:#163b52;
  --teal-ink:#2f5a4e;
  --ink:#2b2b2b;
  --ink-soft:#555;
  --paper:#f4efe5;
  --board:#e7e7e7;
  --night:#131313;
  --white:#ffffff;
  --sans:'Barlow',Arial,sans-serif;
  --display:'Poppins',Arial,sans-serif;
}
*{margin:0;padding:0;box-sizing:border-box}
html,body{width:919px;height:1200px;overflow:hidden}
body{position:relative;background:var(--board);font-family:var(--sans);color:var(--ink)}
.board-backdrop{position:absolute;inset:0}
.brand{position:absolute;left:60px;top:24px;width:290px;text-align:center;color:var(--gold-soft)}
.brand-mark{width:60px;height:72px;margin:0 auto 14px;border:2px solid var(--gold-soft)}
.brand-name{font-family:var(--sans);font-weight:300;font-size:17px;letter-spacing:1.2px;text-transform:uppercase;white-space:nowrap}
.brand-tagline{font-weight:300;font-size:8px;letter-spacing:1px;margin-top:3px;text-transform:uppercase}
.deck-title{position:absolute;left:52px;top:184px;width:305px;text-align:center;line-height:1}
.deck-title .strong{display:block;font-family:var(--display);font-weight:700;font-size:45px;color:var(--gold-soft)}
.deck-title .light{display:block;font-family:var(--display);font-weight:400;font-size:45px;color:var(--white);margin-top:2px}
.hero-slide{position:absolute;left:431px;top:108px;width:358px;height:203px;overflow:hidden;box-shadow:0 6px 18px rgba(0,0,0,.25)}
.section-label{position:absolute;left:0;width:919px;top:441px;text-align:center;font-family:var(--sans);font-weight:400;font-size:27px;color:var(--night);text-shadow:0 2px 8px rgba(90,90,160,.35)}
.slide{position:absolute;width:270px;height:152px;overflow:hidden;background:var(--white)}
.abs{position:absolute}
.thin{font-weight:300}
.tiny{font-size:3.6px;line-height:1.35}
.caps{text-transform:uppercase}
.check{display:inline-block;width:6px;height:6px;border:0.8px solid var(--gold);border-radius:1px;margin-right:3px;vertical-align:middle}
.wordmark{font-size:3.4px;font-weight:400;color:var(--gold);letter-spacing:.3px;text-transform:uppercase}
.quote{font-weight:300;font-size:5px;line-height:1.9;text-align:center}
.tax-list{list-style:none;color:#222}
.tax-row{display:flex;align-items:center;height:16px}
.tax-pct{flex:0 0 33px;font-weight:300;font-size:12.5px;line-height:1;color:var(--teal-ink)}
.tax-label{font-size:4.2px;line-height:1.2}
</style>
</head>
<body>

<svg class="board-backdrop" width="919" height="1200" viewBox="0 0 919 1200" role="img" aria-label="Dark photo of raised hands at a sunset gathering behind the title">
  <defs>
    <linearGradient id="nightFade" x1="0" y1="0" x2="1" y2="1">
      <stop offset="0" stop-color="#1b1b1b"/>
      <stop offset="0.55" stop-color="#2a2520"/>
      <stop offset="1" stop-color="#101010"/>
    </linearGradient>
  </defs>
  <polygon points="0,0 919,0 0,539" fill="url(#nightFade)"/>
</svg>

<header class="brand">
  <div class="brand-mark"></div>
  <div class="brand-name">Cresthaven Vale Goods</div>
  <div class="brand-tagline">"Cultivating the future"</div>
</header>

<h1 class="deck-title"><span class="strong">Presentation</span><span class="light">Deck</span></h1>

<section class="hero-slide">
  <svg width="358" height="203" viewBox="0 0 358 203">
    <rect width="358" height="203" fill="var(--gold)"/>
    <path d="M0,10 Q180,32 358,14 L358,188 Q180,172 0,192 Z" fill="var(--navy)" role="img" aria-label="Family portrait shaded in blue"/>
    <path d="M0,8 Q180,30 358,12" stroke="#fff" stroke-width="2.5" fill="none"/>
    <path d="M0,194 Q180,174 358,190" stroke="#fff" stroke-width="2.5" fill="none"/>
  </svg>
  <div class="abs thin" style="left:31px;top:50px;color:#fff;font-size:25px;line-height:1.15;letter-spacing:.5px">CRESTHAVEN V-G &amp;<br>THE CITY OF<br>NYSSA</div>
  <div class="abs quote" style="left:228px;top:138px;width:115px;color:#fff;font-size:6.2px">"Community In Action, Control,<br>Transparent and Economic<br>Development"</div>
</section>

<h2 class="section-label">Powerpoint Presentation</h2>

<!-- Row 1 -->
<section class="slide" style="left:37px;top:500px;background:linear-gradient(90deg,var(--gold),var(--gold-pale))">
  <svg class="abs" width="270" height="152" viewBox="0 0 270 152">
    <polygon points="0,0 50,0 50,40 0,80" fill="#8a5c3c" role="img" aria-label="Town welcome sign"/>
    <polygon points="0,80 40,40 80,80 0,152" fill="#3d5466" role="img" aria-label="Lake at sunset"/>
    <polygon points="80,80 150,152 60,152" fill="#b57a4a" role="img" aria-label="Family group outdoors"/>
    <polygon points="82,30 134,82 82,134 30,82" fill="#3a3a3a"/>
  </svg>
  <div class="abs wordmark" style="left:50px;top:79px;width:64px;text-align:center;color:#ddd">Cresthaven Vale Goods</div>
  <div class="abs thin" style="left:118px;top:20px;width:150px;text-align:center;color:#fff8e8;font-size:16px;line-height:1.2">CRESTHAVEN V-G &amp;<br>THE CITY OF<br>NYSSA</div>
  <div class="abs quote" style="left:170px;top:98px;width:95px;color:#fff;font-size:4.6px">"Community In Action, Control,<br>Transparent and Economic<br>Development"</div>
</section>

<section class="slide" style="left:324px;top:500px;background:#f5f1ea">
  <svg class="abs" width="270" height="152" viewBox="0 0 270 152" role="img" aria-label="Faded family portrait">
    <rect x="150" y="10" width="120" height="135" fill="#e9dfcf"/>
    <path d="M0,0 L270,0 L270,6 Q135,0 0,12 Z" fill="var(--gold)"/>
    <path d="M0,12 Q135,0 270,6" stroke="#333" stroke-width="1.5" fill="none"/>
    <path d="M0,135 Q135,150 270,142 L270,152 L0,152 Z" fill="var(--gold)"/>
    <path d="M0,131 Q135,146 270,138" stroke="#333" stroke-width="1.5" fill="none"/>
  </svg>
  <div class="abs thin" style="left:23px;top:36px;color:#444;font-size:18px;line-height:1.2">CRESTHAVEN V-G &amp;<br>THE CITY OF<br>NYSSA</div>
  <div class="abs quote" style="left:170px;top:104px;width:95px;color:#555;font-size:4.6px">"Community In Action, Control,<br>Transparent and Economic<br>Development"</div>
</section>

<section class="slide" style="left:612px;top:500px">
  <div class="abs" style="left:22px;top:0;width:228px;height:44px;background:var(--navy-deep);border-radius:0 0 24px 24px"></div>
  <div class="abs thin" style="left:42px;top:7px;color:#dfe8ee;font-size:6.2px">Ethics is knowing the difference</div>
  <div class="abs caps" style="left:54px;top:17px;color:#fff;font-size:6px">Between what you have a right to do</div>
  <div class="abs" style="left:92px;top:25px;color:var(--gold);font-size:11px">and what is right to do</div>
  <div class="abs thin" style="left:21px;top:60px;color:var(--gold);font-size:11.5px">COMPANY SUMMARY</div>
  <p class="abs tiny" style="left:22px;top:76px;width:235px;color:#333">Cresthaven Vale Goods will be modeled after my father and grandfather business practices. One of our main goals will be to earn the community of Nyssa's trust through our actions. Community involvement, drug awareness, and becoming a member of the chamber would honor our company and being able to give back to a community that gave me a safe and amazing childhood.</p>
  <p class="abs tiny" style="left:22px;top:99px;width:235px;color:#333"><span class="check"></span>pledge#1; CVG cant stress this enough and remains committed to keeping cannabis 100% out of the hands of all youths.</p>
  <p class="abs tiny" style="left:22px;top:113px;width:235px;color:#333"><span class="check"></span>Pledge#2; CVG has no interest or would we ever try to change ones believes or core values and is not interested in making this a moral or ethical issue. Marijuana is a drug and it needs to be controlled and we feel that taking control and holding others accountable is the best way to handle this situation.</p>
  <div class="abs wordmark" style="left:115px;top:140px;width:40px;text-align:center">Cresthaven Vale Goods</div>
</section>

<!-- Row 2 -->
<section class="slide" style="left:37px;top:673px;background:var(--paper)">
  <div class="abs" style="left:18px;top:18px;font-family:var(--display);font-weight:700;color:var(--gold);font-size:21px;letter-spacing:2px">MISSION</div>
  <div class="abs thin" style="left:66px;top:42px;color:var(--gold);font-size:13px;letter-spacing:1px">statement</div>
  <p class="abs tiny" style="left:15px;top:70px;width:145px;color:#444;font-size:4.2px">To create a name brand of the highest of quality, with an emphasis on medical applications that holds CONTROL and the strict regulations governed by the city of Nyssa and the SSRB.</p>
  <p class="abs tiny" style="left:15px;top:95px;width:145px;color:#444;font-size:4.2px">In doing this; we will bring economic development, growth, family waged jobs and several new tax benefits that can greatly increase the prosperity of Nyssa.</p>
  <div class="abs" role="img" aria-label="Gold company seal" style="left:175px;top:38px;width:120px;height:120px;border-radius:50%;background:radial-gradient(circle at 40% 40%,#f3cf7d,#b98a2e)"></div>
  <div class="abs" style="left:196px;top:58px;width:70px;height:70px;border-radius:50%;border:1.5px solid #8a6420"></div>
</section>

<section class="slide" style="left:324px;top:673px">
  <div class="abs" style="left:12px;top:0;width:108px;height:152px;background:#333"></div>
  <div class="abs" style="left:20px;top:29px;color:#fff;font-weight:700;font-size:7px">PRODUCTION</div>
  <ul class="abs tiny" style="left:24px;top:41px;width:92px;color:#eee;font-size:3.3px">
    <li>Transparent</li><li>Strictly indoor; out of sight- out of mind</li><li>Fully compliant nyssa/ssrb of full control of environment</li><li>Smell and other nuisances</li><li>Secrecy</li><li>Medical Application</li>
  </ul>
  <div class="abs" style="left:20px;top:96px;color:#fff;font-weight:700;font-size:7px">WHOLESALE</div>
  <ul class="abs tiny" style="left:24px;top:107px;width:92px;color:#eee;font-size:3.3px">
    <li>Sent out of the area for profiting into products that benefit the medical applications.</li><li>Wholesalers out of the area to keep away from our youths</li>
  </ul>
  <div class="abs" style="left:134px;top:13px;color:var(--gold);font-weight:700;font-size:10.5px">Know Your Business</div>
  <div class="abs thin" style="left:185px;top:25px;color:var(--gold);font-size:8.5px">License Types</div>
  <div class="abs" style="left:120px;top:41px;width:138px;border-top:.7px solid #666"></div>
  <div class="abs" style="left:130px;top:46px;color:var(--gold);font-size:4.5px">SSRB</div>
  <div class="abs tiny" style="left:130px;top:54px;width:128px;color:#333;font-size:3px">
    <b>Producer:</b> Ability to plant, cultivate, grow, harvest, and dry marijuana.<br>
    <b>Processor:</b> Ability to process, compound, or convert marijuana into cannabinoid products, concentrates, and/or extracts.<br>
    <b>Wholesale:</b> Can purchase quantities of marijuana from other licensed facilities and sell the products to licensed retailers, processors, producers, other wholesalers, or research certificate holders.<br>
    <b>Laboratory:</b> Accredited and responsible for testing marijuana items for pesticides, solvents or residual solvents, cannabinoid concentration, and for microbiological or other contaminants.<br>
    <b>Retail:</b> Can sell or deliver marijuana items directly to consumers.<br>
    <b>Research Certificate:</b> Ability to research marijuana for the purpose of benefiting the state's cannabis industry, medical research, or public health and safety.
  </div>
</section>

<section class="slide" style="left:612px;top:670px">
  <div class="abs thin" style="left:0;top:14px;width:270px;text-align:center;color:#333;font-size:13.5px">TYPE OF LICENSSING</div>
  <div class="abs wordmark" style="left:228px;top:10px;width:34px;text-align:center">Cresthaven Vale Goods</div>
  <div class="abs" style="left:22px;top:52px;width:83px;height:80px;background:#fff;border-radius:8px;box-shadow:0 1px 6px rgba(0,0,0,.15)"></div>
  <div class="abs" style="left:34px;top:41px;width:60px;height:16px;background:#fff;border-radius:9px;box-shadow:0 1px 4px rgba(0,0,0,.12);color:var(--gold);font-size:5px;text-align:center;line-height:16px">Production</div>
  <ul class="abs caps" style="left:32px;top:68px;width:70px;list-style:none;color:#333;font-size:3.2px;line-height:1.3">
    <li style="margin-bottom:4px"><span class="check" style="width:5px;height:5px"></span>Indoor tier 1 or tier 2 max</li>
    <li style="margin-bottom:4px"><span class="check" style="width:5px;height:5px"></span>Out of sight out of mind</li>
    <li style="margin-bottom:4px"><span class="check" style="width:5px;height:5px"></span>Not interested in outdoor production</li>
    <li style="margin-bottom:4px"><span class="check" style="width:5px;height:5px"></span>Contain smell</li>
    <li><span class="check" style="width:5px;height:5px"></span>Strong security</li>
  </ul>
  <div class="abs" style="left:127px;top:54px;width:120px;height:80px;background:#fff;border-radius:8px;box-shadow:0 1px 6px rgba(0,0,0,.15)"></div>
  <div class="abs" style="left:157px;top:43px;width:60px;height:16px;background:#fff;border-radius:9px;box-shadow:0 1px 4px rgba(0,0,0,.12);color:var(--gold);font-size:5px;text-align:center;line-height:16px">Wholesale</div>
  <ul class="abs caps" style="left:136px;top:66px;width:108px;list-style:none;color:#333;font-size:3.1px;line-height:1.3">
    <li style="margin-bottom:3px"><span class="check" style="width:5px;height:5px"></span>Ship, test and wholesale product out of the area</li>
    <li style="margin-bottom:3px"><span class="check" style="width:5px;height:5px"></span>Pledges to not create problems for the city of Nyssa; no extra traffic of any kind</li>
    <li style="margin-bottom:3px"><span class="check" style="width:5px;height:5px"></span>No advertising</li>
    <li style="margin-bottom:3px"><span class="check" style="width:5px;height:5px"></span>Never glorifying to our youth</li>
    <li style="margin-bottom:3px"><span class="check" style="width:5px;height:5px"></span>Wholesale out of the area to guarantee product gets turned into processing and medical applications</li>
    <li><span class="check" style="width:5px;height:5px"></span>In support of abolishment of the blackmarket</li>
  </ul>
</section>

<!-- Row 3 -->
<section class="slide" style="left:37px;top:845px">
  <svg class="abs" width="270" height="152" viewBox="0 0 270 152">
    <rect width="270" height="152" fill="#8d5a3a" role="img" aria-label="Welcome to Nyssa town sign among trees"/>
    <polygon points="0,0 168,0 80,152 0,152" fill="var(--gold)"/>
  </svg>
  <div class="abs thin" style="left:12px;top:10px;color:#fff;font-size:13px;line-height:1.15">BUSINESS<br>ASSUMPTIONS &amp;<br>GOALS</div>
  <div class="abs thin" style="left:11px;top:85px;width:100px;color:#fff;font-size:6px;line-height:1.3">OPPORTUNITY, CREATING GROWTH AND PROSPERITY TO THE COMMUNITY OF NYSSA</div>
  <div class="abs wordmark" style="left:2px;top:143px;color:#fff">Cresthaven Vale Goods</div>
</section>

<section class="slide" style="left:327px;top:845px">
  <div class="abs thin" style="left:16px;top:14px;color:var(--gold);font-size:18px">GOALS</div>
  <div class="abs" style="left:60px;top:80px;width:140px;height:140px;border-radius:50%;background:var(--gold-soft)"></div>
  <div class="abs" role="img" aria-label="Family walking on a beach at sunset" style="left:22px;top:60px;width:68px;height:68px;transform:rotate(45deg);border-radius:12px;background:linear-gradient(160deg,#f7c56c,#6c7a8e)"></div>
  <div class="abs wordmark" style="left:2px;top:143px;color:#fff">Cresthaven Vale Goods</div>
  <ul class="abs" style="left:128px;top:12px;width:138px;list-style:none;color:#333;font-size:4.2px;line-height:1.25">
    <li style="height:16px"><span class="check" style="border-color:#444;width:8px;height:8px"></span>Integral part of the community of Nyssa (Like my grandfather and father before me).</li>
    <li style="height:16px"><span class="check" style="border-color:#444;width:8px;height:8px"></span>Family waged jobs</li>
    <li style="height:16px"><span class="check" style="border-color:#444;width:8px;height:8px"></span>Full employee benefits</li>
    <li style="height:16px"><span class="check" style="border-color:#444;width:8px;height:8px"></span>Join Nyssa chamber of commerce</li>
    <li style="height:22px"><span class="check" style="border-color:#444;width:8px;height:8px"></span>Increase tax revenue ; City Sales tax &amp; cvg Community in action fund</li>
    <li style="height:22px"><span class="check" style="border-color:#444;width:8px;height:8px"></span>Generate and raise funds for swimming pool and other activites</li>
    <li><span class="check" style="border-color:#444;width:8px;height:8px"></span>Organizing awareness, fundraisers for drug abuse, and other areas in which the community could use extra funding</li>
  </ul>
</section>

<section class="slide" style="left:612px;top:845px;background:linear-gradient(180deg,#2a2a2a,#4a4640)" role="img" aria-label="Hands holding a note about change">
  <div class="abs thin" style="left:0;top:12px;width:270px;text-align:center;color:#fff;font-size:15px">Market review and tax benifit</div>
  <div class="abs thin" style="left:0;top:38px;width:270px;text-align:center;color:#fff;font-size:8px">At the request of the council</div>
  <div class="abs" style="left:20px;top:50px;width:230px;text-align:center;color:#eee;font-size:3.5px">( I will have a market analysis done on Nyssa with factual numbers and data of tax benefits that a recreational indoor production facility could create for the community )</div>
  <div class="abs" style="left:5px;top:78px;width:62px;height:68px;background:#fff;border-radius:6px"></div>
  <div class="abs" style="left:71px;top:78px;width:62px;height:68px;background:#fff;border-radius:6px"></div>
  <div class="abs" style="left:137px;top:78px;width:62px;height:68px;background:#fff;border-radius:6px"></div>
  <div class="abs" style="left:203px;top:78px;width:62px;height:68px;background:#fff;border-radius:6px"></div>
  <div class="abs" style="left:20px;top:62px;width:32px;height:32px;border-radius:50%;background:#fff;border:3px solid #eee"><div style="margin:6px;width:14px;height:14px;border-radius:3px;background:var(--navy)"></div></div>
  <div class="abs" style="left:86px;top:62px;width:32px;height:32px;border-radius:50%;background:#fff;border:3px solid #eee"><div style="margin:6px;width:14px;height:14px;border-radius:3px;background:var(--navy)"></div></div>
  <div class="abs" style="left:152px;top:62px;width:32px;height:32px;border-radius:50%;background:#fff;border:3px solid #eee"><div style="margin:6px;width:14px;height:14px;border-radius:3px;background:var(--navy)"></div></div>
  <div class="abs" style="left:218px;top:62px;width:32px;height:32px;border-radius:50%;background:#fff;border:3px solid #eee"><div style="margin:6px;width:14px;height:14px;border-radius:50%;background:var(--gold)"></div></div>
  <div class="abs" style="left:5px;top:108px;width:62px;text-align:center;color:#222;font-size:8.5px;font-weight:500;line-height:1.35">3% city<br>sales tax</div>
  <div class="abs" style="left:71px;top:102px;width:62px;text-align:center;color:#222;font-size:8px;line-height:1.3"><span style="font-size:3.8px;font-weight:600">Conservative base point around</span><br><b style="font-size:9px">$100,000</b><br>a month</div>
  <div class="abs" style="left:137px;top:104px;width:62px;text-align:center;color:#222;font-size:8px;line-height:1.2"><span style="font-size:3.8px;font-weight:600">Community action fund</span><br><b>donating</b><br>another<br><b style="font-size:10px">3%</b></div>
  <div class="abs" style="left:203px;top:104px;width:62px;text-align:center;color:#222;font-size:8.5px;line-height:1.4"><span style="font-size:3.8px">Potential grand total of</span><br><b>$6,000 a month</b> <span style="font-size:3.8px">to Nyssa</span></div>
</section>

<!-- Row 4 -->
<section class="slide" style="left:37px;top:1017px;background:#f5f5f5">
  <div class="abs" role="img" aria-label="Illustration area" style="left:22px;top:30px;width:80px;height:80px;border-radius:50%;background:#dcdcdc"></div>
  <div class="abs thin" style="left:128px;top:12px;color:var(--teal-ink);font-size:10.5px;line-height:1.3">Where Do The Taxes On<br>Rec Pot Go In Oregon?</div>
  <ul class="abs tax-list" style="left:128px;top:46px;width:140px">
    <li class="tax-row"><span class="tax-pct">40%</span><span class="tax-label">To Common School Fund</span></li>
    <li class="tax-row"><span class="tax-pct">20%</span><span class="tax-label">To Mental Health Alcoholism<br>And Drug Services</span></li>
    <li class="tax-row"><span class="tax-pct">15%</span><span class="tax-label">To State Police</span></li>
    <li class="tax-row"><span class="tax-pct">10%</span><span class="tax-label">To Cities For Enforcement Of The Measure</span></li>
    <li class="tax-row"><span class="tax-pct">10%</span><span class="tax-label">To Counties For Enforcement Of<br>The Measure</span></li>
    <li class="tax-row"><span class="tax-pct">5%</span><span class="tax-label">To State Care Agency For Alcohol<br>And Drug Abuse Prevention</span></li>
  </ul>
</section>

<section class="slide" style="left:327px;top:1015px;background:var(--navy-deep)">
  <div class="abs" role="img" aria-label="Soft green foliage backdrop" style="left:0;top:0;width:150px;height:152px;background:linear-gradient(90deg,#3e5a48,rgba(22,59,82,0))"></div>
  <div class="abs thin" style="left:20px;top:62px;color:#fff;font-size:16px;line-height:1.2">Overview<br>statement</div>
  <svg class="abs" style="left:152px;top:24px" width="16" height="110" viewBox="0 0 16 110">
    <g fill="none" stroke="var(--gold)" stroke-width="1.6">
      <rect x="1" y="1" width="13" height="13" rx="2"/><path d="M4 7l3 3 8-9"/>
      <rect x="1" y="46" width="13" height="13" rx="2"/><path d="M4 52l3 3 8-9"/>
      <rect x="1" y="93" width="13" height="13" rx="2"/><path d="M4 99l3 3 8-9"/>
    </g>
  </svg>
  <p class="abs tiny" style="left:170px;top:22px;width:92px;color:#aab;font-size:3.2px;line-height:2">Operating in a professional manner while following all state guidelines in which the council must approve and oversee every step.</p>
  <p class="abs tiny" style="left:170px;top:52px;width:92px;color:#aab;font-size:3.2px;line-height:2">Our plan is not to change minds. We want to earn trust through action, honest reporting and steady support for local families and youth.</p>
  <p class="abs tiny" style="left:170px;top:108px;width:92px;color:#aab;font-size:3.2px;line-height:2">Bring a safe, controlled business that keeps product away from minors, never advertises and gives back to the people of Nyssa.</p>
  <div class="abs wordmark" style="left:125px;top:143px;width:34px;text-align:center">Cresthaven Vale Goods</div>
</section>

<section class="slide" style="left:610px;top:1015px;background:#fafafa">
  <div class="abs" role="img" aria-label="Family walking at golden hour" style="left:16px;top:16px;width:137px;height:125px;background:linear-gradient(160deg,#f1b447,#e9c27a)"></div>
  <div class="abs thin" style="left:33px;top:55px;color:#fff;font-size:10px;line-height:1.35">My internal<br>gratitude and<br>Deep thoughts<br>w/ Garrett Pascoe:</div>
  <div class="abs" style="left:219px;top:23px;width:31px;height:6px;border-radius:3px;background:#333"></div>
  <div class="abs" style="left:144px;top:27px;width:117px;height:55px;background:#fff;box-shadow:0 1px 5px rgba(0,0,0,.15)"></div>
  <p class="abs tiny" style="left:148px;top:32px;width:108px;color:#888;font-size:3.2px">I know what the community and the council have faced before. Thank you for your patience, your questions and the care you show for this town and its future.</p>
  <div class="abs" style="left:191px;top:84px;width:31px;height:6px;border-radius:3px;background:#333"></div>
  <div class="abs" style="left:118px;top:88px;width:112px;height:42px;background:#fff;box-shadow:0 1px 5px rgba(0,0,0,.15)"></div>
  <p class="abs tiny" style="left:128px;top:95px;width:94px;color:#888;font-size:3.2px">Thank you for giving me your time today, and letting me present the future of Nyssa to my fellow community and council members.</p>
</section>

</body>
</html>
```